Billboard for personal injury chiropractors office

We are a personal injury chiropractor clinic.
I need a Billboard with the company name as the dominating factor. Also a smaller picture or 2 of something creative, like a car accident or an arm in a cast off to the sides.
We Like something Clean and Simple and Eye Catching. Please make the picture Small and Off To The Side. The MAIN FOCUS areas are the… name Varden Chiropractic Clinic
At the top CAR ACCIDENT INJURY?
AND at the bottom our number 418-27-FLEXA.
Dr.Milo R. Varden in bold somewhere with the word chiropractor under the doctors name in a text.

Im open to red lettering on white backgrounds, red on yellow backgrounds and I'm also open to reds blues white and yellow. I'd prefer yellow if used be across the bottom.

I am uploading a very rough draft of what we are after along with a screenshot of the tv commercial showing the yellow

DO NOT USE THE LOGO ON THE COMMERCIAL. I JUST WANT THE NAME TYPED LIKE ON SAMPLE BILLBOARD.

Industry/Entity Type

Chiropractic

Colors
0054AA
0677BA
7BADD7
CADEEF
E8F1F8
FFF300
FFF600
FEFA6F
FFFEC7
FFFEE8
EB3D1F
EC4F4E
F09395
F8D3D4
FCEDEE

Requirements
Must have
• Eye catching ,bold

```html
<!DOCTYPE html>
<html lang="en">
<head>
<meta charset="utf-8">
<title>Varden Chiropractic Clinic – Billboard</title>
<link rel="stylesheet" href="https://fonts.googleapis.com/css2?family=Antonio:wght@300&family=Bebas+Neue&family=Poppins:wght@600;700&display=swap">
<style>
  :root {
    --stage: #000000;
    --red: #c00000;
    --yellow: #fff500;
    --white: #ffffff;
    --ink: #0a0a0a;
  }
  html, body {
    margin: 0;
    width: 1200px;
    height: 1200px;
    overflow: hidden;
    background: var(--stage);
  }
  .billboard {
    position: absolute;
    left: 99px;
    top: 401px;
    width: 1002px;
    height: 292px;
    overflow: hidden;
  }
  .billboard-shapes {
    position: absolute;
    inset: 0;
    display: block;
  }
  .headline,
  .clinic-name,
  .doctor-name,
  .call-line {
    position: absolute;
    right: 27px;
    margin: 0;
    white-space: nowrap;
    text-align: right;
    line-height: 1;
  }
  .headline {
    top: 31px;
    font-family: "Antonio", sans-serif;
    font-weight: 300;
    font-size: 66px;
    color: var(--yellow);
    letter-spacing: -0.5px;
  }
  .clinic-name {
    top: 116px;
    font-family: "Bebas Neue", sans-serif;
    font-weight: 400;
    font-size: 56px;
    color: var(--white);
  }
  .doctor-name {
    top: 179px;
    font-family: "Poppins", sans-serif;
    font-weight: 600;
    font-size: 46px;
    color: var(--ink);
  }
  .call-line {
    top: 236px;
    right: 14px;
    font-family: "Poppins", sans-serif;
    color: var(--white);
  }
  .call-label {
    font-weight: 600;
    font-size: 29px;
    color: var(--yellow);
    margin-right: 8px;
  }
  .call-number {
    font-weight: 700;
    font-size: 46px;
    letter-spacing: 0.5px;
  }
</style>
</head>
<body>
  <section class="billboard">
    <svg class="billboard-shapes" width="1002" height="292" viewBox="0 0 1002 292">
      <defs>
        <linearGradient id="photo-tone" x1="0" y1="0" x2="1" y2="1">
          <stop offset="0" stop-color="#e0a066"/>
          <stop offset="0.35" stop-color="#6b5b55"/>
          <stop offset="1" stop-color="#1f1d1c"/>
        </linearGradient>
      </defs>
      <g role="img" aria-label="Photo: wrecked car behind a man in a dark shirt with his arm in a blue cast">
        <polygon points="0,0 392,0 516,292 0,292" fill="url(#photo-tone)"/>
      </g>
      <polygon class="divider" points="373,0 392,0 516,292 497,292" fill="var(--white)"/>
      <polygon class="red-panel" points="392,0 1002,0 1002,292 516,292" fill="var(--red)"/>
      <polygon class="yellow-band" points="465,173 1002,173 1002,229 489,229" fill="var(--yellow)"/>
    </svg>

    <h1 class="headline">CAR ACCIDENT INJURY?</h1>
    <h2 class="clinic-name">VARDEN CHIROPRACTIC CLINIC</h2>
    <p class="doctor-name">Dr.Milo R. Varden</p>
    <p class="call-line"><span class="call-label">Call Now</span><span class="call-number">418-552-0917</span></p>
  </section>
</body>
</html>
```